Lantern Grill

we need a flyer design. for an A4 sheet folded into 3 layers/pages.
for an Indian fast food take away. Please use up to date UK standard menu design.
Any more info needed can contact us anytime by email.
word document of item for the flyer attached.

Target Market(s)

Indian Food lovers

Industry/Entity Type

Indian Restaurant

Font styles to use
Decorative
Script

Colors
cbe087
abd036
fbf289
f37022

Requirements
Must have
• Can you please bleed the menu so that I can show it to the printer guy
Nice to have
• modern menu

```html
<!DOCTYPE html>
<html lang="en">
<head>
<meta charset="utf-8">
<title>Lantern Grill – Delivery Menu</title>
<link rel="stylesheet" href="https://fonts.googleapis.com/css2?family=Cinzel:wght@400;700&family=Kaushan+Script&family=Open+Sans:wght@400;600;700&display=swap">
<style>
  :root {
    --backdrop: #e6d8b8;
    --wood-dark: #3b1b0b;
    --wood: #5c2f15;
    --wood-light: #7a4424;
    --green: #abd036;
    --green-soft: #cbe087;
    --yellow: #fbf289;
    --orange: #f37022;
    --band: #cbb77c;
    --ink: #1d1208;
    --cream: #f4ead2;
    --white: #ffffff;
  }
  * { box-sizing: border-box; margin: 0; padding: 0; }
  html, body { width: 1200px; height: 917px; overflow: hidden; }
  body {
    background: var(--backdrop);
    font-family: "Open Sans", sans-serif;
    color: var(--ink);
    position: relative;
  }
  .flyer {
    position: absolute;
    left: 40px; top: 62px;
    width: 1120px; height: 792px;
    display: flex;
    box-shadow: 0 6px 18px rgba(60, 40, 10, .25);
  }
  .panel {
    width: 373.33px; height: 100%;
    position: relative;
    overflow: hidden;
    background:
      linear-gradient(90deg, rgba(0,0,0,.18), rgba(255,255,255,.04) 30%, rgba(0,0,0,.12) 60%, rgba(255,255,255,.05) 85%, rgba(0,0,0,.15)),
      linear-gradient(180deg, var(--wood-light), var(--wood) 45%, var(--wood-dark));
  }
  .panel + .panel { border-left: 1px solid rgba(0,0,0,.25); }

  .green-box {
    background: var(--green);
    border: 3px solid var(--orange);
    outline: 4px solid var(--wood-dark);
    position: absolute;
  }
  .drinks { left: 20px; top: 18px; width: 333px; height: 134px; padding: 8px 16px; }
  .section-heading {
    font-family: "Cinzel", serif; font-weight: 700;
    font-size: 22px; line-height: 28px; letter-spacing: .5px;
  }
  .drinks-list { list-style: none; margin-top: 4px; font-weight: 700; font-size: 14px; line-height: 20px; }
  .drinks-list li { display: flex; justify-content: space-between; }
  .drinks-list .size { font-weight: 400; }

  .allergy { left: 20px; top: 166px; width: 333px; height: 268px; padding: 12px 14px; font-size: 12.5px; line-height: 16px; }
  .allergy-title { text-align: center; font-weight: 700; font-size: 18px; line-height: 22px; margin: 8px 0 3px; }
  .allergy-list { font-weight: 700; font-size: 12.5px; line-height: 17px; text-align: center; }

  .photo { position: absolute; }
  .photo-samosa {
    left: 0; bottom: 0; width: 100%; height: 344px;
    background: radial-gradient(ellipse at 40% 55%, #cfa35c, #e5c890 45%, #f1ead9 80%);
  }

  .band {
    background: var(--band);
    font-family: "Cinzel", serif; font-weight: 700;
    color: var(--ink);
    display: flex; align-items: center; justify-content: space-between;
    padding: 0 24px;
  }
  .band-pizza { height: 52px; font-size: 24px; }
  .band-pizza .sizes { font-size: 22px; }
  .pizza-list { list-style: none; padding: 10px 20px 0; color: var(--cream); }
  .pizza-list li { margin-bottom: 6px; }
  .pizza-name { color: var(--orange); font-weight: 700; font-size: 14px; line-height: 18px; display: block; }
  .pizza-row { display: flex; justify-content: space-between; gap: 12px; font-size: 12.5px; line-height: 15px; }
  .price { white-space: nowrap; align-self: flex-end; }
  .band-deal { height: 44px; justify-content: center; font-size: 24px; position: absolute; left: 0; right: 0; top: 356px; }
  .deal-one { left: 20px; top: 416px; width: 333px; height: 166px; padding: 8px 18px; }
  .deal-two { left: 20px; top: 598px; width: 333px; height: 182px; padding: 8px 18px; }
  .deal-title { font-family: "Cinzel", serif; font-weight: 700; font-size: 18px; line-height: 21px; }
  .deal-list { font-size: 13px; line-height: 16px; padding-left: 20px; margin-top: 4px; }

  .brand {
    background: var(--white);
    height: 160px;
    display: flex; align-items: center; justify-content: center; gap: 12px;
  }
  .brand-mark { width: 16px; height: 16px; background: var(--orange); border-radius: 50%; }
  .brand-name { font-family: "Cinzel", serif; font-weight: 700; font-size: 38px; color: var(--ink); }
  .cover-body { padding: 18px 22px 0; color: var(--cream); text-align: center; }
  .tagline { font-family: "Kaushan Script", cursive; font-size: 34px; color: var(--cream); }
  .address { font-family: "Cinzel", serif; font-weight: 700; font-size: 17px; text-align: right; margin-top: 4px; }
  .hours { font-family: "Cinzel", serif; font-weight: 700; font-size: 32px; line-height: 34px; color: var(--yellow); margin-top: 18px; }
  .phone { font-family: "Cinzel", serif; font-weight: 700; font-size: 18px; text-align: left; margin-top: 22px; white-space: nowrap; overflow: hidden; }
  .delivery-title { font-family: "Cinzel", serif; font-weight: 700; font-size: 22px; margin-top: 12px; }
  .delivery-areas { font-family: "Cinzel", serif; font-weight: 700; font-size: 14px; line-height: 18px; }
  .photo-biryani {
    left: 0; bottom: 0; width: 100%; height: 230px;
    background: radial-gradient(ellipse at 50% 45%, #f5efe2 0%, #e0a857 35%, #c8862e 65%, #7a4a1e 100%);
  }
</style>
</head>
<body>
  <main class="flyer">
    <section class="panel panel-info">
      <div class="green-box drinks">
        <h2 class="section-heading">Soft Drinks</h2>
        <ul class="drinks-list">
          <li><span>Lemon Fizz 1.00</span><span class="size">330ml can</span></li>
          <li><span>Orange Burst 1.00</span><span class="size">330ml can</span></li>
          <li><span>Cola 1.00</span><span class="size">330ml can</span></li>
          <li><span>Diet Cola 1.00</span><span class="size">330ml can</span></li>
        </ul>
      </div>
      <div class="green-box allergy">
        <p>We cook all our meals to order, and each main course is cooked separately, so our pots and pans get used throughout service. Our equipment is washed thoroughly between each preparation, but we cannot guarantee some allergens will not be present. If you are extremely susceptible to nuts for example, please inform us when ordering. No MSG is used in any of our cooking.</p>
        <h3 class="allergy-title">Allergens</h3>
        <p class="allergy-list">Eggs | Nuts | Mustard | Crustaceans | Soya | Fish<br>Milk / Yoghurt | Gluten | Sesame Seeds | Celery<br>Lupin | Peanuts | Molluscs | Sulpher dioxide</p>
      </div>
      <div class="photo photo-samosa" role="img" aria-label="Photo of golden samosas with one opened on a fork beside a dip"></div>
    </section>

    <section class="panel panel-menu">
      <div class="band band-pizza"><span>Pizza</span><span class="sizes">10” / 12”</span></div>
      <ul class="pizza-list">
        <li><span class="pizza-name">Margarita</span><div class="pizza-row"><span>Tomato and mozzarella cheese</span><span class="price">4.50/5.00</span></div></li>
        <li><span class="pizza-name">Mexican</span><div class="pizza-row"><span>Cheese, pepperoni, peppers, onions, jalapenos and chilli</span><span class="price">6.00/7.00</span></div></li>
        <li><span class="pizza-name">Hawaiian</span><div class="pizza-row"><span>Ham, cheese and pineapple</span><span class="price">5.00/6.00</span></div></li>
        <li><span class="pizza-name">Milano</span><div class="pizza-row"><span>Ham, chicken, cheese and sweetcorn, peppers</span><span class="price">6.00/7.00</span></div></li>
        <li><span class="pizza-name">Vegetarian</span><div class="pizza-row"><span>Tomato, cheese, mushroom, onion, pepper, sweetcorn</span><span class="price">5.00/6.00</span></div></li>
        <li><div class="pizza-row"><span class="pizza-name">Garlic Bread</span><span class="price">3.50/4.50</span></div></li>
      </ul>
      <div class="band band-deal">Deal</div>
      <div class="green-box deal-one">
        <h3 class="deal-title">Set Meal B for 1<br>Non-Vegetarian €16.00</h3>
        <ul class="deal-list">
          <li>Chicken tikka starter</li>
          <li>Chicken tikka masala</li>
          <li>Pilau Rice</li>
          <li>Plain Naan</li>
          <li>Popadoms and spiced onions</li>
          <li>Choice of soft drink</li>
        </ul>
      </div>
      <div class="green-box deal-two">
        <h3 class="deal-title">Set Meal for 2 €25.00</h3>
        <ul class="deal-list">
          <li>Onion bhaji</li>
          <li>Chicken tikka starter</li>
          <li>Chicken tikka masala</li>
          <li>Lamb Roganjosh</li>
          <li>2 x Pilau rice</li>
          <li>Plain Naan</li>
          <li>Poppadum with spiced onion</li>
          <li>2 soft drinks</li>
        </ul>
      </div>
    </section>

    <section class="panel panel-cover">
      <header class="brand">
        <span class="brand-mark"></span>
        <span class="brand-name">Lantern Grill</span>
      </header>
      <div class="cover-body">
        <p class="tagline">Kebab – Pizza – Curry</p>
        <p class="address">14 Mill Lane,<br>Dunmore</p>
        <p class="hours">Opening Hours<br>5pm – 10.30pm</p>
        <p class="phone">Phone No# ----------------------</p>
        <p class="delivery-title">Delivery Menu</p>
        <p class="delivery-areas">We delivery to -<br>Kilbrook, Ashford Bridge, Marrowvale</p>
      </div>
      <div class="photo photo-biryani" role="img" aria-label="Photo of chicken biryani rice topped with yoghurt and fresh coriander"></div>
    </section>
  </main>
</body>
</html>
```